Business card design needed

Quiet Haven Network is a not-for- profit organisation which advocates for palliative care in the community and runs a good size volunteer program to the community. We also run day hospice centres, provide massage & podiatry to clients etc. Our current business cards are very old fashioned and a new look is timely to some positive changes bringing the organisation forward.
Updates

Hi everyone, Thank you all so much for submitting your very clever designs.  I will confer with my colleagues tomorrow and hopefully we can make a decision :)

Industry/Entity Type

Massage

Contact Information for Business Card

Miriam Coley
Operations Manager
T 02 6180 4392
M 0417552864
E Miriam@quiethavennet.org.au

Logo Text

Quiet Haven Network Inc

Logo styles of interest
Pictorial/Combination Logo
Requirements
Must have
• Our logo (I think I have attached it, contact me if it didn't work)

```html
<!DOCTYPE html>
<html lang="en">
<head>
<meta charset="utf-8">
<title>Miriam Coley – Business Card</title>
<link rel="stylesheet" href="https://fonts.googleapis.com/css2?family=Questrial&family=Montserrat:wght@600&display=swap">
<style>
  :root {
    --page-bg: #1f2022;
    --card-dark: #2a2e33;
    --card-light: #3b4046;
    --accent-bar: #f2c21b;
    --name-green: #b8c42c;
    --title-grey: #e6e7e8;
    --label-gold: #d9aa1d;
    --block-deep: #c99d27;
    --block-mid: #ebbb2b;
    --block-light: #f9d45a;
    --contact-white: #f4f4f4;
    --icon-ink: #2a2e33;
  }
  html, body {
    margin: 0;
    width: 1200px;
    height: 1050px;
    overflow: hidden;
    background: var(--page-bg);
  }
  .card {
    position: absolute;
    left: 100px;
    top: 220px;
    width: 1000px;
    height: 611px;
    background: linear-gradient(160deg, var(--card-light) 0%, var(--card-dark) 55%, var(--card-dark) 100%);
    box-shadow: 0 18px 40px rgba(0,0,0,0.55);
    overflow: hidden;
    font-family: "Questrial", sans-serif;
  }
  .accent-bar {
    position: absolute;
    left: 44px;
    top: 44px;
    width: 14px;
    height: 96px;
    background: var(--accent-bar);
  }
  .name {
    position: absolute;
    left: 74px;
    top: 38px;
    margin: 0;
    font-size: 40px;
    font-weight: 400;
    color: var(--name-green);
    letter-spacing: 0.5px;
    line-height: 1;
  }
  .job-title {
    position: absolute;
    left: 74px;
    top: 88px;
    margin: 0;
    font-size: 44px;
    color: var(--title-grey);
    line-height: 1;
  }
  .service-block {
    position: absolute;
    left: 640px;
    top: 130px;
    width: 360px;
    height: 118px;
    display: flex;
  }
  .service-block .step-deep { width: 62px; background: var(--block-deep); }
  .service-block .step-mid { width: 52px; background: var(--block-mid); }
  .service-block .step-light { flex: 1; background: var(--block-light); }
  .tagline {
    position: absolute;
    left: 640px;
    top: 266px;
    margin: 0;
    font-size: 28px;
    color: var(--title-grey);
  }
  .person-label {
    position: absolute;
    left: 112px;
    top: 318px;
    margin: 0;
    font-size: 24px;
    color: var(--label-gold);
  }
  .contact-list {
    position: absolute;
    left: 76px;
    top: 360px;
    margin: 0;
    padding: 0;
    list-style: none;
    font-family: "Montserrat", sans-serif;
    font-weight: 600;
    font-size: 24px;
    color: var(--contact-white);
  }
  .contact-list li {
    display: flex;
    align-items: center;
    height: 34px;
  }
  .contact-list svg {
    width: 24px;
    height: 24px;
    margin-right: 14px;
    flex: none;
  }
</style>
</head>
<body>
  <article class="card">
    <div class="accent-bar"></div>
    <h1 class="name">MIRIAM COLEY</h1>
    <h2 class="job-title">OPERATIONS MANAGER</h2>

    <div class="service-block" aria-hidden="true">
      <div class="step-deep"></div>
      <div class="step-mid"></div>
      <div class="step-light"></div>
    </div>
    <p class="tagline">Provide Massage &amp; Podiatry</p>

    <p class="person-label">Person Name</p>
    <ul class="contact-list">
      <li>
        <svg viewBox="0 0 24 24" aria-label="Telephone">
          <circle cx="12" cy="12" r="12" fill="var(--accent-bar)"/>
          <path d="M8 6.5c-1 .6-1.6 1.8-1 3.4 1 2.8 3.3 5.1 6.1 6.1 1.6.6 2.8 0 3.4-1l-2.2-1.8-1.4 1c-1.4-.7-2.5-1.8-3.2-3.2l1-1.4z" fill="var(--icon-ink)"/>
        </svg>
        02 6180 4392
      </li>
      <li>
        <svg viewBox="0 0 24 24" aria-label="Mobile">
          <circle cx="12" cy="12" r="12" fill="var(--accent-bar)"/>
          <rect x="8.5" y="5" width="7" height="14" rx="1.4" fill="var(--icon-ink)"/>
          <rect x="9.8" y="7" width="4.4" height="8" fill="var(--accent-bar)"/>
        </svg>
        04 1755 2864
      </li>
      <li>
        <svg viewBox="0 0 24 24" aria-label="Email">
          <circle cx="12" cy="12" r="12" fill="var(--accent-bar)"/>
          <rect x="6" y="8" width="12" height="8.5" rx="1" fill="var(--icon-ink)"/>
          <path d="M6.5 8.6 12 13l5.5-4.4" fill="none" stroke="var(--accent-bar)" stroke-width="1.2"/>
        </svg>
        Miriam@quiethavennet.org.au
      </li>
    </ul>
  </article>
</body>
</html>
```